Qorby Labs

I am a CBD Manufacturer I would have a site more laid out in a lab format
current site is qorbylabs.example what Id like is a site like tarnwellabs.example

Target Market(s)

Any one needing cbd oil and finished goods

Coding

Coded - Design and coding required

Number of Pages Required

1 page

```html
<!DOCTYPE html>
<html lang="en">
<head>
<meta charset="utf-8">
<title>Qorby Labs</title>
<link href="https://fonts.googleapis.com/css2?family=Montserrat:wght@400;600;700;800&family=Open+Sans:wght@400;600&display=swap" rel="stylesheet">
<style>
:root{
  --gold:#e9b51f;
  --gold-dark:#c99a12;
  --cream:#fdf4d6;
  --beige:#ecdcc0;
  --ink:#222222;
  --muted:#6b6b6b;
  --white:#ffffff;
  --footer:#cfa32a;
}
*{box-sizing:border-box;margin:0;padding:0}
html,body{width:1200px;height:4296px;overflow:hidden}
body{font-family:"Open Sans",Arial,sans-serif;color:var(--ink);background:var(--white);position:relative}
h1,h2,h3,h4,.brand,.btn,.nav a{font-family:"Montserrat",Arial,sans-serif}
.abs{position:absolute}
.btn{display:inline-block;background:var(--gold);color:var(--white);font-size:14px;font-weight:600;padding:10px 26px;border-radius:3px}

/* header */
.topbar{left:0;top:0;width:1200px;height:36px;background:var(--white)}
.topbar .band{position:absolute;left:600px;top:0;width:600px;height:36px;background:var(--gold)}
.socials{position:absolute;right:40px;top:7px;display:flex;gap:8px}
.socials span{width:22px;height:22px;background:var(--white);border-radius:3px;opacity:.9}
.header{left:0;top:36px;width:1200px;height:64px;display:flex;align-items:center;padding:0 58px}
.brand{font-weight:700;font-size:30px;color:var(--gold);letter-spacing:1px}
.nav{margin-left:auto;display:flex;align-items:center;gap:34px}
.nav a{font-size:12px;font-weight:600;color:var(--ink);text-decoration:none}
.nav a.active{background:var(--gold);color:var(--white);padding:8px 14px;border-radius:2px}
.nav .login{background:var(--gold);color:var(--white);padding:9px 22px;border-radius:2px}

/* hero */
.hero{left:0;top:100px;width:1200px;height:628px;background:linear-gradient(100deg,#121212 0%,#2b2f2a 45%,#8a9a90 75%,#cfd8d4 100%)}
.hero h1{position:absolute;left:58px;top:200px;color:var(--white);font-size:44px;font-weight:800;line-height:1.15;width:560px}
.hero p{position:absolute;left:58px;top:320px;color:var(--white);font-size:17px}
.hero .btn{position:absolute;left:58px;top:402px;padding:9px 22px}

/* welcome */
.welcome{left:0;top:728px;width:1200px;height:440px;text-align:center}
.welcome h4{margin-top:86px;font-size:14px;font-weight:600}
.welcome .brand{display:block;font-size:30px;margin-top:4px}
.welcome p{width:440px;margin:8px auto 0;font-size:11px;color:var(--muted);line-height:1.5}
.features{position:absolute;left:150px;top:228px;width:900px}
.features .line{position:absolute;left:80px;right:80px;top:86px;height:2px;background:var(--gold)}
.feature{position:absolute;width:200px;text-align:center}
.feature .icon{width:56px;height:56px;margin:0 auto}
.feature .dot{width:30px;height:30px;border-radius:50%;background:var(--gold);margin:16px auto 0}
.feature h3{font-size:13px;font-weight:700;margin-top:16px}

/* benefits */
.benefits{left:0;top:1184px;width:1200px;height:456px;background:var(--cream);border-top:3px solid var(--gold)}
.benefits h2{position:absolute;left:86px;top:80px;font-size:22px;font-weight:700}
.benefits ul{position:absolute;left:86px;top:130px;width:380px;list-style:none}
.benefits li{position:relative;padding-left:20px;font-size:11px;color:var(--muted);line-height:1.6;margin-bottom:16px}
.benefits li::before{content:"";position:absolute;left:0;top:6px;width:7px;height:7px;border-radius:50%;background:var(--gold)}
.benefits .btn{position:absolute;left:86px;top:362px;padding:9px 22px}
.benefits .photo{position:absolute;left:648px;top:96px;width:340px;height:300px;background:linear-gradient(135deg,#dfe9ee,#9fb7a0 60%,#c9d8cf)}

/* knowledge */
.knowledge-title{left:0;top:1712px;width:1200px;text-align:center;font-size:24px;font-weight:700}
.kblock h3{font-size:24px;font-weight:700;color:var(--gold)}
.kblock p{font-size:11px;color:var(--muted);line-height:1.6;margin-top:8px}
.shade{background:var(--beige)}
.swatches{left:14px;top:2924px;display:flex;flex-direction:column;gap:6px}
.swatches span{width:74px;height:36px}

/* products */
.products{left:0;top:3140px;width:1200px;height:540px;background:var(--cream)}
.products h2{text-align:center;font-size:24px;font-weight:700;margin-top:56px}
.cards{position:absolute;left:60px;top:102px;display:flex;gap:32px}
.card{width:246px;text-align:center}
.card .box{position:relative;height:290px;background:var(--white);border:1px solid #eadfb8}
.card .img{position:absolute;left:58px;top:40px;width:130px;height:210px;border-radius:6px}
.card .tag{position:absolute;right:12px;top:10px;font-size:11px;color:var(--gold);font-weight:600}
.card .cart{position:absolute;left:50%;top:122px;transform:translateX(-50%);padding:8px 18px;font-size:13px}
.stars{margin-top:18px;color:var(--gold);font-size:15px;letter-spacing:2px}
.stars .off{color:#cccccc}
.card h4{font-size:15px;font-weight:600;margin-top:4px}
.card .price{font-size:13px;color:var(--muted);margin-top:4px}

/* customers */
.customers{left:0;top:3690px;width:1200px;height:270px}
.customers h2{position:absolute;left:150px;top:80px;font-size:24px;font-weight:700;line-height:1.3}
.customers .partner{position:absolute;left:448px;top:54px;width:120px;height:150px;background:#c8472c;border-radius:6px}
.customers p{position:absolute;left:728px;top:90px;width:320px;font-size:11px;color:var(--muted);line-height:1.6}

/* footer */
.footer{left:0;top:3960px;width:1200px;height:336px;background:var(--footer);color:var(--white)}
.fcol{position:absolute;top:44px}
.fcol h4{font-size:15px;font-weight:700;margin-bottom:12px}
.fcol p,.fcol li{font-size:11px;line-height:1.7}
.fcol ul{list-style:none}
.footer .brand{color:var(--white);font-size:32px;display:block;margin-bottom:10px}
.newsletter{display:flex;width:250px;margin-top:4px}
.newsletter span{flex:1;background:var(--white);color:#999;font-size:11px;padding:9px 10px}
.newsletter i{width:34px;background:#e8d08a;display:flex;align-items:center;justify-content:center}
.fsocial{display:flex;gap:8px;margin-top:16px}
.fsocial span{width:26px;height:26px;border-radius:50%;background:var(--ink)}
.copyright{position:absolute;left:0;bottom:0;width:1200px;height:36px;background:var(--gold-dark);text-align:center;font-size:11px;line-height:36px}
</style>
</head>
<body>

<div class="abs topbar"><div class="band"><div class="socials"><span></span><span></span><span></span></div></div></div>

<header class="abs header">
  <div class="brand">Qorby Labs</div>
  <nav class="nav">
    <a class="active">HOME</a><a>COMMUNITY</a><a>SHOP</a><a>WHOLESALE</a><a>CONTACT</a><a class="login">LOGIN</a>
  </nav>
</header>

<section class="abs hero" role="img" aria-label="Lab technician in protective gear examining a hemp sample">
  <h1>ROLLING ON TO THE SCENE</h1>
  <p>We are proud to serve our community</p>
  <span class="btn">Learn More</span>
</section>

<section class="abs welcome">
  <h4>Welcome To</h4>
  <span class="brand">Qorby Labs</span>
  <p>Lorem ipsum is simply dummy text of the printing and typesetting industry. Lorem Ipsum has been the industry's standard dummy text ever since the 1500s.</p>
  <div class="features">
    <div class="line"></div>
    <div class="feature" style="left:0;top:0">
      <svg class="icon" viewBox="0 0 56 56"><circle cx="28" cy="28" r="18" fill="#fff" stroke="#c62828" stroke-width="2"/><path d="M12 22h32M10 28h36M12 34h32" stroke="#c62828" stroke-width="3"/><path d="M14 16a18 18 0 0 1 14-6v18H10a18 18 0 0 1 4-12z" fill="#1e3a8a"/></svg>
      <div class="dot"></div><h3>MADE IN THE USA</h3>
    </div>
    <div class="feature" style="left:350px;top:0">
      <svg class="icon" viewBox="0 0 56 56"><rect x="22" y="6" width="12" height="8" fill="#222"/><rect x="18" y="14" width="20" height="36" rx="3" fill="none" stroke="#222" stroke-width="2.5"/><rect x="22" y="26" width="12" height="12" fill="#222"/></svg>
      <div class="dot"></div><h3>FULL SPECTRUM CBD</h3>
    </div>
    <div class="feature" style="left:700px;top:0">
      <svg class="icon" viewBox="0 0 56 56" fill="none" stroke="#222" stroke-width="2.5"><path d="M22 8h12M25 8v14L14 44a3 3 0 0 0 3 4h22a3 3 0 0 0 3-4L31 22V8"/><path d="M18 36h20"/></svg>
      <div class="dot"></div><h3>LAB TESTED</h3>
    </div>
  </div>
</section>

<section class="abs benefits">
  <h2>BENEFITS OF QORBY LABS CBD</h2>
  <ul>
    <li>All of our products are tested to ensure the best quality CBD available.</li>
    <li>Choose from a wide variety of products and flavors including concentrate, edible, tincture, vape pen, body cream, salve and ointment.</li>
    <li>We use CO2 extraction and a chemical-free extraction process that is environmentally friendly and safe for all of our hemp CBD oil.</li>
  </ul>
  <span class="btn">Learn More</span>
  <div class="photo" role="img" aria-label="Scientist holding a hemp leaf and a dropper bottle"></div>
</section>

<h2 class="abs knowledge-title">KNOWLEDGE IS POWER</h2>

<div class="abs shade" style="left:124px;top:2048px;width:480px;height:104px"></div>
<div class="abs" role="img" aria-label="Researcher inspecting hemp plants" style="left:164px;top:1768px;width:308px;height:320px;background:linear-gradient(135deg,#e4ece6,#7f9f6e 60%,#55784a)"></div>
<div class="abs kblock" style="left:590px;top:1860px;width:380px">
  <h3>WHAT IS CBD?</h3>
  <p>Cannabidiol, also known as CBD, is a phytocannabinoid found in agricultural hemp. Unlike its cousin tetrahydrocannabinol, also known as THC, CBD is non-psychoactive, which means it does not produce feelings of euphoria.</p>
</div>

<div class="abs shade" style="left:692px;top:2360px;width:290px;height:210px"></div>
<div class="abs" role="img" aria-label="Farmer checking hemp crop in a field" style="left:742px;top:2192px;width:306px;height:296px;background:linear-gradient(135deg,#5e8a3e,#9dbb6a 55%,#3f6a2c)"></div>
<div class="abs kblock" style="left:300px;top:2232px;width:380px;text-align:right">
  <h3>IS IT LEGAL?</h3>
  <p>Because all of our CBD products are derived from agricultural hemp and compliant, it is not unlawful to ship across the United States.</p>
</div>

<div class="abs" role="img" aria-label="CBD oil bottle and glass with hemp leaves" style="left:164px;top:2660px;width:306px;height:320px;background:linear-gradient(135deg,#4c6b2e,#a9b85a 55%,#d9c277)"></div>
<div class="abs kblock" style="left:590px;top:2752px;width:380px">
  <h3>IS IT SAFE?</h3>
  <p>CBD has a remarkable safety profile and our labs are geared to ensure high quality, safety, and efficacy of our CBD products. All of our products are derived from agricultural hemp, are non-psychoactive, and are produced with care.</p>
</div>
<div class="abs swatches"><span style="background:var(--gold)"></span><span style="background:var(--gold-dark)"></span><span style="background:#3a3a3a"></span><span style="background:var(--ink)"></span></div>

<section class="abs products">
  <h2>OUR PRODUCTS</h2>
  <div class="cards">
    <div class="card">
      <div class="box"><span class="tag">New</span><div class="img" role="img" aria-label="Vape pen in retail pack" style="background:linear-gradient(180deg,#e6e6e6,#b9b9b9)"></div></div>
      <div class="stars">★★★★★</div><h4>Vape Pen</h4><div class="price">$ 35.00</div>
    </div>
    <div class="card">
      <div class="box"><div class="img" role="img" aria-label="Tin of salve" style="top:60px;left:38px;width:170px;height:170px;border-radius:50%;background:linear-gradient(180deg,#3a3a3a,#111)"></div><span class="btn cart">Add To Cart</span></div>
      <div class="stars">★★★★<span class="off">★</span></div><h4>Salve</h4><div class="price">$ 120.00</div>
    </div>
    <div class="card">
      <div class="box"><span class="tag">15%</span><div class="img" role="img" aria-label="Bottle of lotion" style="left:80px;width:86px;background:linear-gradient(180deg,#2a2a2a,#0d0d0d)"></div></div>
      <div class="stars">★★★★★</div><h4>Lotion</h4><div class="price">$ 36.00</div>
    </div>
    <div class="card">
      <div class="box"><div class="img" role="img" aria-label="Roll on ointment bottle" style="left:92px;width:62px;background:linear-gradient(180deg,#1f1f3a,#0d0d1a)"></div></div>
      <div class="stars">★★★★★</div><h4>Roll On Ointment</h4><div class="price">$ 60.00</div>
    </div>
  </div>
</section>

<section class="abs customers">
  <h2>OUR NEW<br>CUSTOMERS</h2>
  <div class="partner" role="img" aria-label="Halden Works customer badge"></div>
  <p>Lorem ipsum is simply dummy text of the printing and typesetting industry. Lorem Ipsum has been the industry's standard dummy text ever since the 1500s.</p>
</section>

<footer class="abs footer">
  <div class="fcol" style="left:58px;width:240px">
    <span class="brand">Qorby Labs</span>
    <p>Our labs build quality CBD products so every customer gets the highest quality hemp and full spectrum blends. Our products are made using the finest natural ingredients.</p>
  </div>
  <div class="fcol" style="left:340px;width:230px">
    <h4>NOTICE</h4>
    <p>The statements regarding these products have not been evaluated by the Food and Drug Administration. These products are not intended to diagnose, treat, cure or prevent any disease.</p>
  </div>
  <div class="fcol" style="left:612px;width:200px">
    <h4>QUICK LINKS</h4>
    <ul><li>Wholesale</li><li>Customer Satisfaction</li><li>Shipping &amp; Return Policy</li><li>Privacy Policy</li><li>Terms and Services</li></ul>
  </div>
  <div class="fcol" style="left:888px;width:260px">
    <h4>NEWS LETTERS</h4>
    <div class="newsletter"><span>Enter email*</span><i><svg width="14" height="14" viewBox="0 0 14 14"><path d="M1 7l12-6-4 12-2-5z" fill="#fff"/></svg></i></div>
    <div class="fsocial"><span></span><span></span><span></span><span></span></div>
  </div>
  <div class="copyright">© Qorby Labs. 2020. All Right Reserved</div>
</footer>

</body>
</html>
```